Small butcher shop from Austria needs great powerpoint presentation

We are looking for a powerpoint template for our new CI - it should be modern and clear.

Logo (2 Versions), Slogan, Business Card and Car-Wrap-Design already exist. (See documents below.)

We won't use much text. About 50% of the presentation should be pictures, included in different ways.

We are a family business in Upper Austria, only process animals from farms in the immediate vicinity, produce the products by hand, value animal welfare and short transport routes and avoid packaging as much as possible.

The design should be modern and clear.

Font styles to use
Sans Serif

Requirements
Should not have
• Use the red color sparingly. Only use sans serif fonts (Myriad Pro - if possible). The logo needs to be on first and last page only.

```html
<!DOCTYPE html>
<html lang="de">
<head>
<meta charset="utf-8">
<title>Hollmayr Fleischhauerei – Präsentationsvorlage</title>
<link href="https://fonts.googleapis.com/css2?family=Source+Sans+3:wght@300;400;600;700&display=swap" rel="stylesheet">
<style>
:root{
  --board:#e8e8e9;
  --paper:#ffffff;
  --brand:#8c1a2f;
  --ink:#2b2b2f;
  --muted:#8a8a8a;
  --band:#f1f3f8;
  --ornament:#dcdcdc;
}
*{margin:0;padding:0;box-sizing:border-box}
html,body{width:1200px;height:2194px;overflow:hidden}
body{background:var(--board);font-family:"Source Sans 3",sans-serif;color:var(--ink);position:relative}
.slide{position:absolute;width:469px;height:264px;background:var(--paper);overflow:hidden;box-shadow:0 10px 26px rgba(0,0,0,.22)}
.col-l{left:80px}.col-r{left:651px}
.abs{position:absolute}
.photo{position:absolute}
.ornament{position:absolute;width:58px;height:7px;background:var(--ornament);border-radius:4px}
.red{color:var(--brand)}
.title{font-weight:400;line-height:1.12;color:var(--ink)}
.lorem{font-size:5.6px;line-height:1.45;color:var(--muted);text-align:justify;font-weight:300}
.label{font-size:6.5px;font-weight:700;color:var(--ink);text-align:center}
.foot-name{position:absolute;left:34px;top:245px;font-size:5.5px;font-weight:700;color:var(--brand)}
.foot-line{position:absolute;left:85px;top:248px;width:287px;height:1px;background:var(--brand)}
.foot-url{position:absolute;right:34px;top:245px;font-size:5.5px;color:var(--brand)}
.foot-url b{font-weight:700}
.wordmark{position:absolute;font-weight:700;font-size:22px;letter-spacing:2px}
.center{text-align:center}
/* agenda */
.agenda-head{left:224px;top:43px;font-size:13px;letter-spacing:2px;color:var(--brand)}
.agenda-sub{left:224px;top:61px;font-size:4.5px;font-weight:700;letter-spacing:1.6px;line-height:1.3}
.agenda-row{position:absolute;left:232px;height:18px;display:flex;align-items:center;font-size:7px}
.agenda-row .num{width:24px;color:var(--brand);font-size:8px}
.agenda-row .txt{border-left:1px solid #ccc;padding-left:5px;height:18px;display:flex;align-items:center;color:#444}
.jar-name{font-size:10px;color:var(--ink)}
.jar-sub{font-size:5.5px;color:var(--muted);font-weight:300}
.strip-label{position:absolute;top:93px;width:94px;font-size:6.5px;color:var(--brand)}
.strip-sub{position:absolute;top:104px;width:94px;font-size:3.5px;color:#bbb}
.small-label{font-size:6px;color:var(--muted);text-align:center;font-weight:300}
</style>
</head>
<body>

<!-- 1: cover red -->
<section class="slide col-l" style="top:101px;background:var(--brand)">
  <div class="photo" style="left:20px;top:19px;width:429px;height:141px;background:linear-gradient(120deg,#5a2a28,#a44a4a 40%,#c9a59a 60%,#3b2523)" role="img" aria-label="Rohes Steak mit Pfeffer auf dem Grill"></div>
  <div class="wordmark" style="left:80px;top:181px;color:#fff">HOLLMAYR</div>
  <div class="abs title center" style="left:221px;top:175px;width:200px;font-size:22px;color:#fff">Your Presentation<br>Title Goes Here</div>
  <div class="abs" style="left:214px;top:252px;font-size:6px;color:#e6c6cc">www.hollmayr.at</div>
</section>

<!-- 2: cover white -->
<section class="slide col-r" style="top:101px">
  <div class="photo" style="left:20px;top:19px;width:429px;height:141px;background:linear-gradient(180deg,#a8c7e6,#dbe7f1 45%,#7da24a 62%,#4d7a2c)" role="img" aria-label="Kuh auf einer grünen Almwiese unter blauem Himmel"></div>
  <div class="wordmark" style="left:80px;top:181px;color:var(--brand)">HOLLMAYR</div>
  <div class="abs title center" style="left:221px;top:175px;width:200px;font-size:22px">Your Presentation<br><span class="red">Title Goes Here</span></div>
  <div class="abs" style="left:214px;top:252px;font-size:6px;color:var(--muted)">www.hollmayr.at</div>
</section>

<!-- 3: agenda -->
<section class="slide col-l" style="top:389px">
  <div class="photo" style="left:20px;top:20px;width:175px;height:221px;background:radial-gradient(circle at 40% 45%,#9c3b42,#5a2a2a 35%,#0c0c0c 70%)" role="img" aria-label="Dry-Aged-Steak auf Packpapier"></div>
  <div class="abs agenda-head">Agenda</div>
  <div class="abs agenda-sub">All staff meeting,<br>May 15, 2021</div>
  <div class="agenda-row" style="top:86px"><span class="num">01</span><span class="txt">Integrity and respect</span></div>
  <div class="agenda-row" style="top:110px"><span class="num">02</span><span class="txt">Memberships</span></div>
  <div class="agenda-row" style="top:134px"><span class="num">03</span><span class="txt">Education</span></div>
  <div class="agenda-row" style="top:158px"><span class="num">04</span><span class="txt">Consultations</span></div>
  <div class="agenda-row" style="top:182px"><span class="num">05</span><span class="txt">What's ahead</span></div>
  <div class="agenda-row" style="top:206px"><span class="num">06</span><span class="txt">Wins</span></div>
  <div class="foot-name">Fleischhauerei</div><div class="foot-line"></div><div class="foot-url"><b>www.hollmayr.at</b> / 4</div>
</section>

<!-- 4: in glass single -->
<section class="slide col-r" style="top:389px">
  <div class="photo" style="left:32px;top:0;width:202px;height:232px;background:linear-gradient(180deg,#d8b25a,#4a4e52 25%,#3a3d40 70%,#b8742e)" role="img" aria-label="Glas Rindsgulasch mit Etikett"></div>
  <div class="abs title" style="left:253px;top:100px;font-size:24px">Hollmayr <span class="red">In Glass</span></div>
  <div class="ornament" style="left:308px;top:138px" role="img" aria-label="Zierornament"></div>
  <div class="abs jar-name center" style="left:253px;top:160px;width:190px">01 Rinds-<span class="red">gulasch</span></div>
  <div class="abs jar-sub center" style="left:253px;top:180px;width:190px;font-size:7px">Regional und hausgemacht, 450 ml.</div>
  <div class="abs lorem" style="left:253px;top:195px;width:190px">Lorem ipsum dolor sit amet, consectetuer adipiscing elit. Maecenas porttitor congue massa. Fusce posuere, magna sed pulvinar ultricies, purus lectus malesuada libero, sit amet commodo magna eros quis urna.</div>
  <div class="foot-name">Fleischhauerei</div><div class="foot-line"></div><div class="foot-url"><b>www.hollmayr.at</b> / 19</div>
</section>

<!-- 5: in glass pair -->
<section class="slide col-l" style="top:677px">
  <div class="photo" style="left:129px;top:0;width:130px;height:128px;background:linear-gradient(180deg,#d8b25a,#4a4e52 25%,#3a3d40 80%)" role="img" aria-label="Glas Rindsgulasch"></div>
  <div class="photo" style="left:0;top:132px;width:130px;height:106px;background:linear-gradient(180deg,#8aa77a,#4a4e52 30%,#3a3d40)" role="img" aria-label="Glas Kalbsbeuschel"></div>
  <div class="abs" style="left:22px;top:63px"><div class="jar-name">01 Rinds-<span class="red">gulasch</span></div><div class="jar-sub">Regional und hausgemacht, 450 ml.</div></div>
  <div class="abs" style="left:155px;top:180px"><div class="jar-name">02 Kalbs-<span class="red">beuschel</span></div><div class="jar-sub">Regional und hausgemacht, 450 ml.</div></div>
  <div class="abs title center" style="left:296px;top:78px;width:140px;font-size:26px">Hollmayr<br><span class="red">In Glass</span></div>
  <div class="ornament" style="left:337px;top:152px" role="img" aria-label="Zierornament"></div>
  <div class="abs lorem" style="left:302px;top:170px;width:130px">Lorem ipsum dolor sit amet, consectetuer adipiscing elit. Maecenas porttitor congue massa. Fusce posuere, magna sed pulvinar ultricies, purus lectus malesuada libero, sit amet commodo magna eros quis urna.</div>
  <div class="foot-name">Fleischhauerei</div><div class="foot-line"></div><div class="foot-url"><b>www.hollmayr.at</b> / 20</div>
</section>

<!-- 6: in glass row -->
<section class="slide col-r" style="top:677px">
  <div class="abs title" style="left:32px;top:17px;font-size:25px">Hollmayr <span class="red">In Glass</span></div>
  <div class="abs lorem" style="left:213px;top:19px;width:226px">Lorem ipsum dolor sit amet, consectetuer adipiscing elit. Maecenas porttitor congue massa. Fusce posuere, magna sed pulvinar ultricies, purus lectus malesuada libero, sit amet commodo magna eros quis urna.</div>
  <div class="ornament" style="left:205px;top:55px" role="img" aria-label="Zierornament"></div>
  <div class="strip-label" style="left:15px">01 Rinds-gulasch</div>
  <div class="strip-label" style="left:109px">02 Kalbs-beuschel</div>
  <div class="strip-label" style="left:203px">03 Kalbs-beuschel</div>
  <div class="strip-label" style="left:297px">04 Kalbs-beuschel</div>
  <div class="strip-label" style="left:391px">05 Kalbs-beuschel</div>
  <div class="strip-sub" style="left:15px">Regional und hausgemacht, 450 ml</div>
  <div class="strip-sub" style="left:109px">Regional und hausgemacht, 450 ml</div>
  <div class="strip-sub" style="left:203px">Regional und hausgemacht, 450 ml</div>
  <div class="strip-sub" style="left:297px">Regional und hausgemacht, 450 ml</div>
  <div class="strip-sub" style="left:391px">Regional und hausgemacht, 450 ml</div>
  <div class="photo" style="left:0;top:117px;width:94px;height:147px;background:linear-gradient(180deg,#d8b25a,#3e4245 30%,#a0642c)" role="img" aria-label="Glas Rindsgulasch"></div>
  <div class="photo" style="left:94px;top:117px;width:94px;height:147px;background:linear-gradient(180deg,#8fb07a,#3e4245 30%,#8a7a4a)" role="img" aria-label="Glas Kalbsbeuschel"></div>
  <div class="photo" style="left:188px;top:117px;width:94px;height:147px;background:linear-gradient(180deg,#9ec2dc,#3e4245 30%,#6a6a5a)" role="img" aria-label="Glas Schweinsbeuschel"></div>
  <div class="photo" style="left:282px;top:117px;width:94px;height:147px;background:linear-gradient(180deg,#9a4fb0,#3e4245 30%,#9a4a2a)" role="img" aria-label="Glas Pasta asciutta"></div>
  <div class="photo" style="left:376px;top:117px;width:93px;height:147px;background:linear-gradient(180deg,#5aa86a,#3e4245 30%,#a0582a)" role="img" aria-label="Glas Gulaschsuppe"></div>
</section>

<!-- 7: dry aged beef -->
<section class="slide col-l" style="top:965px">
  <div class="abs title center" style="left:32px;top:100px;width:180px;font-size:14px;line-height:1.35">Dry Aged Beef<br><span class="red">die angeblich besten<br>Steaks der Welt</span></div>
  <div class="ornament" style="left:93px;top:164px" role="img" aria-label="Zierornament"></div>
  <div class="abs lorem" style="left:43px;top:180px;width:160px">Die Fleischhauerei Hollmayr bietet Dry Aged Beef von Rindern aus der Region. Die Tiere sind auf österreichischen Bauernhöfen geboren, werden dort gefüttert und schlussendlich zum nähesten Schlachthof transportiert.</div>
  <div class="photo" style="left:221px;top:30px;width:211px;height:200px;background:radial-gradient(circle at 50% 45%,#a8404a,#7a4a3a 35%,#0d0d0d 70%)" role="img" aria-label="Dry-Aged-Steak auf Packpapier"></div>
  <div class="foot-name">Fleischhauerei</div><div class="foot-line"></div><div class="foot-url"><b>www.hollmayr.at</b> / 5</div>
</section>

<!-- 8: rohwürste three -->
<section class="slide col-r" style="top:965px">
  <div class="abs title" style="left:27px;top:26px;font-size:25px">Rohwürste</div>
  <div class="ornament" style="left:62px;top:62px" role="img" aria-label="Zierornament"></div>
  <div class="abs lorem" style="left:31px;top:82px;width:111px">Lorem ipsum dolor sit amet, consectetuer adipiscing elit. Maecenas porttitor congue massa. Fusce posuere, magna sed pulvinar ultricies, purus lectus malesuada libero, sit amet commodo magna eros quis urna. Lorem ipsum dolor sit amet, consectetuer adipiscing elit. Maecenas porttitor congue massa. Fusce posuere, magna sed pulvinar ultricies, purus lectus malesuada libero, sit amet commodo magna eros quis urna. Lorem ipsum</div>
  <div class="photo" style="left:156px;top:82px;width:95px;height:98px;background:linear-gradient(135deg,#2b3338,#c98a5c 45%,#2b3338)" role="img" aria-label="Rohwürste auf dunklem Grund"></div>
  <div class="photo" style="left:264px;top:82px;width:95px;height:98px;background:linear-gradient(135deg,#2b3338,#d0956a 50%,#2b3338)" role="img" aria-label="Rohwürste mit Kürbiskernen"></div>
  <div class="photo" style="left:373px;top:82px;width:96px;height:98px;background:linear-gradient(135deg,#2b3338,#c47e54 45%,#2b3338)" role="img" aria-label="Gemischte Rohwürste"></div>
  <div class="abs small-label" style="left:156px;top:189px;width:95px">Bauernossi</div>
  <div class="abs small-label" style="left:264px;top:189px;width:95px">Bauernossi mit<br>Kürbiskernen</div>
  <div class="abs small-label" style="left:373px;top:189px;width:96px">Bauernossi<br>gemischt</div>
  <div class="foot-name">Fleischhauerei</div><div class="foot-line"></div><div class="foot-url"><b>www.hollmayr.at</b> / 22</div>
</section>

<!-- 9: rohwürste grid -->
<section class="slide col-l" style="top:1253px">
  <div class="abs label" style="left:155px;top:32px;width:88px">Hauswürstel mit Pfeffer</div>
  <div class="abs label" style="left:243px;top:32px;width:88px">Rindsknackerl Pfeffer</div>
  <div class="photo" style="left:155px;top:44px;width:88px;height:65px;background:linear-gradient(135deg,#2a2f33,#a89a82 50%,#2a2f33)" role="img" aria-label="Hauswürstel mit Pfeffer"></div>
  <div class="photo" style="left:243px;top:44px;width:88px;height:65px;background:linear-gradient(135deg,#2a2f33,#8f8674 50%,#2a2f33)" role="img" aria-label="Rindsknackerl mit Pfeffer"></div>
  <div class="photo" style="left:243px;top:132px;width:88px;height:88px;background:linear-gradient(135deg,#2a2f33,#d2502a 50%,#2a2f33)" role="img" aria-label="Rindsknackerl mit Chili"></div>
  <div class="photo" style="left:331px;top:132px;width:88px;height:88px;background:linear-gradient(135deg,#2a2f33,#b84a2e 50%,#2a2f33)" role="img" aria-label="Gemischte Rindsknackerl"></div>
  <div class="abs label" style="left:243px;top:224px;width:88px">Rindsknackerl Chili</div>
  <div class="abs label" style="left:331px;top:224px;width:88px">Rindsknackerl gemischt</div>
  <div class="abs title center" style="left:45px;top:155px;width:160px;font-size:24px">Rohwürste</div>
  <div class="ornament" style="left:96px;top:189px" role="img" aria-label="Zierornament"></div>
  <div class="foot-name">Fleischhauerei</div><div class="foot-line"></div><div class="foot-url"><b>www.hollmayr.at</b> / 23</div>
</section>

<!-- 10: rohwürste row -->
<section class="slide col-r" style="top:1253px">
  <div class="abs title" style="left:27px;top:26px;font-size:25px">Rohwürste</div>
  <div class="ornament" style="left:62px;top:62px" role="img" aria-label="Zierornament"></div>
  <div class="abs lorem" style="left:187px;top:32px;width:261px">Lorem ipsum dolor sit amet, consectetuer adipiscing elit. Maecenas porttitor congue massa. Fusce posuere, magna sed pulvinar ultricies, purus lectus malesuada libero, sit amet commodo magna eros quis urna. Lorem ipsum dolor sit amet, consectetuer adipiscing elit. Maecenas porttitor congue massa. Fusce posuere, magna sed pulvinar ultricies, purus lectus malesuada libero, sit amet commodo magna eros quis urna. Lorem ipsum</div>
  <div class="abs small-label" style="left:117px;top:120px;width:88px">Hauswürstel mit Pfeffer</div>
  <div class="abs small-label" style="left:205px;top:120px;width:88px">Rindsknackerl Pfeffer</div>
  <div class="abs small-label" style="left:293px;top:120px;width:88px">Rindsknackerl Chili</div>
  <div class="abs small-label" style="left:381px;top:120px;width:88px">Rindsknackerl gemischt</div>
  <div class="photo" style="left:117px;top:132px;width:88px;height:94px;background:linear-gradient(135deg,#2a2f33,#a89a82 50%,#2a2f33)" role="img" aria-label="Hauswürstel mit Pfeffer"></div>
  <div class="photo" style="left:205px;top:132px;width:88px;height:94px;background:linear-gradient(135deg,#2a2f33,#8f8674 50%,#2a2f33)" role="img" aria-label="Rindsknackerl mit Pfeffer"></div>
  <div class="photo" style="left:293px;top:132px;width:88px;height:94px;background:linear-gradient(135deg,#2a2f33,#d2502a 50%,#2a2f33)" role="img" aria-label="Rindsknackerl mit Chili"></div>
  <div class="photo" style="left:381px;top:132px;width:88px;height:94px;background:linear-gradient(135deg,#2a2f33,#b84a2e 50%,#2a2f33)" role="img" aria-label="Gemischte Rindsknackerl"></div>
  <div class="foot-name">Fleischhauerei</div><div class="foot-line"></div><div class="foot-url"><b>www.hollmayr.at</b> / 24</div>
</section>

<!-- 11: suppeneinlagen pair -->
<section class="slide col-l" style="top:1541px">
  <div class="foot-name">Fleischhauerei</div><div class="foot-line"></div>
  <div class="abs title center" style="left:26px;top:137px;width:170px;font-size:22px">Suppeneinlagen</div>
  <div class="ornament" style="left:82px;top:164px" role="img" aria-label="Zierornament"></div>
  <div class="abs lorem" style="left:32px;top:179px;width:164px">Lorem ipsum dolor sit amet, consectetuer adipiscing elit. Maecenas porttitor congue massa. Fusce posuere, magna sed pulvinar ultricies, purus lectus malesuada libero, sit amet commodo magna eros quis urna.</div>
  <div class="photo" style="left:215px;top:2px;width:123px;height:218px;background:radial-gradient(circle at 50% 45%,#e7b45e,#b8853a 35%,#2a3035 65%)" role="img" aria-label="Kaspressknödel"></div>
  <div class="abs label" style="left:215px;top:226px;width:123px">Kaspressknödel</div>
  <div class="abs label" style="left:347px;top:32px;width:122px">Leberknödel</div>
  <div class="photo" style="left:347px;top:44px;width:122px;height:220px;background:radial-gradient(circle at 50% 55%,#7a4a34,#5e3a2a 30%,#c8c8c8 55%,#6a6a6a)" role="img" aria-label="Leberknödel"></div>
</section>

<!-- 12: suppeneinlagen row -->
<section class="slide col-r" style="top:1541px">
  <div class="abs title" style="left:32px;top:45px;font-size:22px">Suppeneinlagen</div>
  <div class="abs lorem" style="left:225px;top:49px;width:208px">Lorem ipsum dolor sit amet, consectetuer adipiscing elit. Maecenas porttitor congue massa. Fusce posuere, magna sed pulvinar ultricies, purus lectus malesuada libero, sit amet commodo magna eros quis urna.</div>
  <div class="ornament" style="left:196px;top:86px" role="img" aria-label="Zierornament"></div>
  <div class="abs label" style="left:0;top:120px;width:156px">Kaspressknödel</div>
  <div class="abs label" style="left:156px;top:120px;width:157px">Leberknödel</div>
  <div class="abs label" style="left:313px;top:120px;width:156px">Fleischstrudel</div>
  <div class="photo" style="left:0;top:134px;width:156px;height:105px;background:radial-gradient(circle at 50% 55%,#e7b45e,#b8853a 28%,#2a3035 55%)" role="img" aria-label="Kaspressknödel"></div>
  <div class="photo" style="left:156px;top:134px;width:157px;height:105px;background:radial-gradient(circle at 50% 55%,#7a4a34,#5e3a2a 25%,#c8c8c8 50%,#6a6a6a)" role="img" aria-label="Leberknödel"></div>
  <div class="photo" style="left:313px;top:134px;width:156px;height:105px;background:radial-gradient(ellipse at 50% 55%,#d89a52,#a8702e 30%,#2a3035 58%)" role="img" aria-label="Fleischstrudel"></div>
  <div class="foot-name">Fleischhauerei</div><div class="foot-line"></div><div class="foot-url"><b>www.hollmayr.at</b> / 26</div>
</section>

<!-- 13: catering -->
<section class="slide col-l" style="top:1829px">
  <div class="abs" style="left:0;top:0;width:469px;height:54px;background:var(--band)"></div>
  <div class="abs title center" style="left:0;top:14px;width:469px;font-size:19px;color:#444">Catering, Platten- und Brötchenservice</div>
  <div class="abs center" style="left:0;top:38px;width:469px;font-size:5.5px;color:#555">Sie feiern - wir liefern ihr Essen!</div>
  <div class="photo" style="left:11px;top:62px;width:109px;height:86px;background:linear-gradient(135deg,#c9a66a,#e8d8c0 40%,#a8403a)" role="img" aria-label="Aufschnittplatte"></div>
  <div class="photo" style="left:123px;top:62px;width:109px;height:86px;background:linear-gradient(135deg,#6a4a3a,#d8b8a8 50%,#8a6a5a)" role="img" aria-label="Wurstplatte"></div>
  <div class="photo" style="left:236px;top:62px;width:109px;height:86px;background:linear-gradient(135deg,#7aa04a,#e8e0d0 50%,#c84a3a)" role="img" aria-label="Salatplatte"></div>
  <div class="photo" style="left:348px;top:62px;width:109px;height:86px;background:linear-gradient(135deg,#5a3a2a,#c86a3a 50%,#3a2a20)" role="img" aria-label="Gebratenes auf Platte"></div>
  <div class="photo" style="left:11px;top:151px;width:109px;height:86px;background:linear-gradient(135deg,#b8904a,#e8d8b0 50%,#6a5a3a)" role="img" aria-label="Platte mit Beilagen"></div>
  <div class="photo" style="left:123px;top:151px;width:109px;height:86px;background:linear-gradient(135deg,#4a7a3a,#e8e8e0 50%,#2a3a4a)" role="img" aria-label="Belegte Brötchen"></div>
  <div class="photo" style="left:236px;top:151px;width:109px;height:86px;background:linear-gradient(135deg,#c84a2a,#e8c0a0 50%,#5a3a2a)" role="img" aria-label="Bratenplatte"></div>
  <div class="photo" style="left:348px;top:151px;width:109px;height:86px;background:linear-gradient(135deg,#c88a8a,#e8d0c0 50%,#8a4a4a)" role="img" aria-label="Schinkenplatte"></div>
  <div class="foot-name">Fleischhauerei</div><div class="foot-line"></div><div class="foot-url"><b>www.hollmayr.at</b> / 27</div>
</section>

<!-- 14: title slide -->
<section class="slide col-r" style="top:1829px">
  <div class="photo" style="left:49px;top:44px;width:171px;height:184px;background:radial-gradient(circle at 45% 55%,#e8a8a0,#c87a6a 35%,#b8703a 55%,#3a4a2a)" role="img" aria-label="Gekochter Schinken mit Kräutern"></div>
  <div class="abs title center" style="left:259px;top:84px;width:160px;font-size:26px">Your Title<br><span class="red">Slide Here</span></div>
  <div class="ornament" style="left:310px;top:157px" role="img" aria-label="Zierornament"></div>
  <div class="abs center" style="left:259px;top:167px;width:160px;font-size:8px;line-height:1.45;color:#444">Lorem ipsum dolor sit amet,<br>consectetuer adipiscing elit.</div>
  <div class="abs lorem" style="left:261px;top:196px;width:162px">Lorem ipsum dolor sit amet, consectetuer adipiscing elit. Maecenas porttitor congue massa. Fusce posuere, magna sed pulvinar ultricies, purus lectus malesuada libero, sit amet commodo magna eros quis urna.</div>
  <div class="foot-name">Fleischhauerei</div><div class="foot-line"></div><div class="foot-url"><b>www.hollmayr.at</b> / 28</div>
</section>

</body>
</html>
```